We have a company that provide sandblasted stone products. Example: numbers for houses. Also we sell cultured stone,brick natural stone to the contractor,homeowner. We need to get a business card that describe our product and service. In the original idea we had an old fashion chisel striking through the x in velmirox.

Reason: We realized that 2 days was not enough time for the competion to be open many of the designers may be to busy and require more time to compete.

Industry/Entity Type

It Company

Logo Text

Velmirox

```html
<!DOCTYPE html>
<html lang="en">
<head>
<meta charset="utf-8">
<title>Velmirox Business Card</title>
<link href="https://fonts.googleapis.com/css2?family=Arimo:wght@400&display=swap" rel="stylesheet">
<style>
  :root {
    --backdrop: #e6e6e4;
    --card-white: #ffffff;
    --stone-light: #9a9a98;
    --stone-mid: #7d7d7b;
    --stone-dark: #5f5f5d;
    --ink: #1c1c1c;
    --logo-ink: #3f3f3e;
    --card-shadow: rgba(0, 0, 0, 0.18);
  }
  * { margin: 0; padding: 0; box-sizing: border-box; }
  html, body {
    width: 1200px;
    height: 900px;
    overflow: hidden;
    background: var(--backdrop);
  }
  body {
    font-family: "Arimo", Arial, sans-serif;
    color: var(--ink);
  }
  .canvas {
    position: relative;
    width: 1200px;
    height: 900px;
    display: flex;
    align-items: center;
    justify-content: center;
    gap: 60px;
  }
  .card {
    position: relative;
    width: 520px;
    height: 300px;
    overflow: hidden;
    box-shadow: 0 6px 18px var(--card-shadow);
  }
  .card-front { background: var(--card-white); }
  .stone-fill {
    position: absolute;
    inset: 0;
    width: 100%;
    height: 100%;
  }
  .contact-block {
    position: absolute;
    top: 26px;
    left: 34px;
    font-size: 13px;
    line-height: 15px;
  }
  .holder {
    position: absolute;
    right: 28px;
    bottom: 26px;
    text-align: right;
  }
  .holder-name {
    font-size: 21px;
    line-height: 24px;
  }
  .holder-title {
    font-size: 13px;
    line-height: 16px;
  }
  .card-back .wordmark {
    position: absolute;
    inset: 0;
    display: flex;
    align-items: center;
    justify-content: center;
    font-size: 58px;
    letter-spacing: 1px;
    color: var(--logo-ink);
  }
</style>
</head>
<body>
<main class="canvas">

  <section class="card card-front" aria-label="Business card front">
    <svg class="stone-fill" viewBox="0 0 520 300" preserveAspectRatio="none" role="img" aria-label="Grey sandblasted stone texture">
      <defs>
        <linearGradient id="stoneFront" x1="0" y1="0" x2="1" y2="1">
          <stop offset="0" stop-color="var(--stone-light)"/>
          <stop offset="0.6" stop-color="var(--stone-mid)"/>
          <stop offset="1" stop-color="var(--stone-dark)"/>
        </linearGradient>
      </defs>
      <path d="M0 0 H20 C18 150 160 270 340 300 H0 Z" fill="url(#stoneFront)"/>
    </svg>

    <address class="contact-block" style="font-style: normal;">
      <div>Suite 5</div>
      <div>123 Street, Canada</div>
      <div>Tel: 1233 456</div>
      <div>Mob: 1245678</div>
      <div>Email: yourname@yourcompany.com</div>
      <div>www.yourcompany.com</div>
    </address>

    <div class="holder">
      <div class="holder-name">John Doe</div>
      <div class="holder-title">Chief Executive Officer</div>
    </div>
  </section>

  <section class="card card-back" aria-label="Business card back">
    <svg class="stone-fill" viewBox="0 0 520 300" preserveAspectRatio="none" role="img" aria-label="Grey sandblasted stone surface">
      <defs>
        <linearGradient id="stoneBack" x1="0" y1="0" x2="1" y2="1">
          <stop offset="0" stop-color="var(--stone-mid)"/>
          <stop offset="0.5" stop-color="var(--stone-light)"/>
          <stop offset="1" stop-color="var(--stone-mid)"/>
        </linearGradient>
      </defs>
      <rect width="520" height="300" fill="url(#stoneBack)"/>
    </svg>
    <div class="wordmark">VELMIROX</div>
  </section>

</main>
</body>
</html>
```